Diesel Fitting/Mechanical Company Needs a new Business Card

We would like a new business card that showcases our logo and business information.

Industry/Entity Type

Business

Contact Information for Business Card

317 Wattlegum Street
PO Box 2968 GREYSTONE RIDGE QLD 4736
Phone: 47319852 Fax: 47319743 Mobile: 0438915267 ABN: 53 719 062 384

Requirements
Must have
• The following email addresses:
• admin@tkservicing.com.au , sales@tkservicing.com.au , accounts@tkservicing.com.au , parts@tkservicing.com.au , office@tkservicing.com.au
• Also need to have the website: www.tkservicing.com.au

```html
<!DOCTYPE html>
<html lang="en">
<head>
<meta charset="utf-8">
<title>TK Servicing – Business Card</title>
<link rel="stylesheet" href="https://fonts.googleapis.com/css2?family=Cousine&family=Noto+Sans:wght@400;700&display=swap">
<style>
  :root {
    --backdrop: #4689c9;
    --card: #ffffff;
    --ink: #111111;
    --address-red: #8e1b1b;
    --contact-red: #e3221c;
    --brand-orange: #f07a22;
    --brand-yellow: #f6b91a;
    --card-shadow: rgba(0, 0, 0, 0.35);
  }
  * { box-sizing: border-box; margin: 0; padding: 0; }
  html, body {
    width: 1200px;
    height: 1200px;
    overflow: hidden;
    background: var(--backdrop);
  }
  .sheet {
    width: 1200px;
    height: 1200px;
    display: flex;
    flex-direction: column;
    align-items: center;
    justify-content: center;
    gap: 40px;
  }
  .card {
    position: relative;
    width: 840px;
    height: 512px;
    background: var(--card);
    box-shadow: 6px 8px 14px var(--card-shadow);
    font-family: "Noto Sans", Verdana, sans-serif;
  }

  /* Contact side */
  .card-back .brand {
    position: absolute;
    left: 50px;
    top: 190px;
    display: flex;
    align-items: center;
    gap: 12px;
  }
  .brand-dot {
    width: 34px;
    height: 34px;
    border-radius: 50%;
    background: var(--brand-yellow);
  }
  .brand-name {
    font-weight: 700;
    color: var(--brand-orange);
    font-size: 44px;
    line-height: 1;
  }
  .address {
    position: absolute;
    left: 430px;
    top: 88px;
    font-family: "Cousine", "Courier New", monospace;
    font-size: 19px;
    line-height: 1.2;
    color: var(--address-red);
    font-style: normal;
  }
  .contact-lines {
    position: absolute;
    left: 450px;
    top: 218px;
    font-family: "Cousine", "Courier New", monospace;
    font-size: 17px;
    line-height: 1.25;
    color: var(--contact-red);
    list-style: none;
  }
  .contact-lines .label {
    display: inline-block;
    width: 80px;
  }
  .website {
    position: absolute;
    left: 470px;
    top: 330px;
    font-family: "Cousine", "Courier New", monospace;
    font-size: 17px;
    color: var(--contact-red);
  }
  .emails {
    position: absolute;
    font-size: 13px;
    line-height: 1.3;
    color: var(--ink);
    list-style: none;
  }
  .emails-right { right: 150px; top: 408px; text-align: right; }
  .emails-left { left: 300px; top: 462px; }

  /* Brand side */
  .card-front {
    display: flex;
    align-items: center;
    justify-content: center;
  }
  .card-front .brand {
    display: flex;
    align-items: center;
    gap: 24px;
  }
  .card-front .brand-dot {
    width: 90px;
    height: 90px;
  }
  .card-front .brand-name {
    font-size: 92px;
  }
</style>
</head>
<body>
<main class="sheet">
  <section class="card card-back" aria-label="Business card, contact side">
    <div class="brand">
      <span class="brand-dot"></span>
      <span class="brand-name">TK Servicing</span>
    </div>
    <address class="address">
      317 Wattlegum Street,<br>
      PO Box 2968,<br>
      GREYSTONE RIDGE<br>
      QLD 4736
    </address>
    <ul class="contact-lines">
      <li><span class="label">Phone:</span>47319852</li>
      <li><span class="label">Fax:</span>47319743</li>
      <li><span class="label">Mobile:</span>0438915267</li>
      <li><span class="label">ABN:</span>53 719 062 384</li>
    </ul>
    <p class="website">website: www.tkservicing.com.au</p>
    <ul class="emails emails-right">
      <li>sales@tkservicing.com.au</li>
      <li>parts@tkservicing.com.au</li>
      <li>office@tkservicing.com.au</li>
    </ul>
    <ul class="emails emails-left">
      <li>admin@tkservicing.com.au</li>
      <li>accounts@tkservicing.com.au</li>
    </ul>
  </section>

  <section class="card card-front" aria-label="Business card, brand side">
    <div class="brand">
      <span class="brand-dot"></span>
      <span class="brand-name">TK Servicing</span>
    </div>
  </section>
</main>
</body>
</html>
```